Roofing Trade Show - Retractable Banners

We need retractable banners to go beside our table for trade shows and markets. One banner will focus on Homeowners and the other banner will target Commercial Property Managers. We provide roof installation and repairs on several roof types for residential and commercial properties. Our logo color is Teal.
There are 2 Design Guideline files attached but we are open to your artistic design suggestions.
Also included here along are some logo varions and some residential roof images.
We don't have any commercial / industrial rooftop images so royalty free stock photos are fine.
If you have questions, please contact me.
Target Market(s)
Commercial Property Managers and Real Estate Brokers
Industry/Entity Type
Construction
Look and feel

```html
<!DOCTYPE html>
<html lang="en">
<head>
<meta charset="utf-8">
<title>Cove Point Roofing – Commercial Banner</title>
<link href="https://fonts.googleapis.com/css2?family=Poppins:wght@400;600;800;900&display=swap" rel="stylesheet">
<style>
  :root {
    --teal: #0b8f94;
    --teal-deep: #0a8a8f;
    --white: #ffffff;
    --sky-top: #8d8fc4;
    --sky-mid: #b7a8cc;
    --dusk: #e9b7a8;
    --lawn: #5f7a3e;
    --house: #6b6f80;
  }
  * { margin: 0; padding: 0; box-sizing: border-box; }
  html, body { width: 1200px; height: 2836px; overflow: hidden; background: var(--white); }
  body { font-family: "Poppins", sans-serif; color: var(--teal); }
  .banner { position: relative; width: 1200px; height: 2836px; background: var(--white); }

  .brand {
    position: absolute; left: 0; width: 1200px; top: 120px;
    display: flex; justify-content: center; align-items: center; gap: 22px;
  }
  .brand-mark { width: 40px; height: 40px; background: var(--teal); }
  .brand-name { font-weight: 800; font-size: 64px; letter-spacing: 1px; color: var(--teal); line-height: 1; }

  .headline {
    position: absolute; left: 0; width: 1200px; top: 352px;
    text-align: center; font-weight: 900; font-size: 108px; line-height: 96px;
    letter-spacing: -3px; color: var(--teal); text-transform: uppercase;
  }
  .tagline {
    position: absolute; left: 0; width: 1200px; top: 556px;
    text-align: center; font-weight: 400; font-size: 54px; line-height: 64px; color: var(--teal);
  }

  .hero-photo {
    position: absolute; left: 0; top: 639px; width: 1200px; height: 847px;
    background:
      linear-gradient(180deg, rgba(0,0,0,0) 55%, rgba(70,80,95,0.55) 75%, var(--lawn) 88%, #8a8f96 100%),
      linear-gradient(180deg, var(--sky-top) 0%, var(--sky-mid) 35%, var(--dusk) 55%, var(--house) 70%);
  }

  .info-panel { position: absolute; left: 0; top: 1486px; width: 1200px; height: 1350px; background: var(--teal); color: var(--white); }

  .audience {
    position: absolute; left: 0; width: 1200px; top: 60px;
    text-align: center; font-weight: 800; font-size: 50px; line-height: 72px; letter-spacing: -0.5px;
  }
  .list-col { position: absolute; top: 252px; list-style: none; }
  .list-col.types { left: 229px; }
  .list-col.services { left: 690px; }
  .list-title { font-weight: 800; font-size: 50px; line-height: 60px; margin-bottom: 28px; }
  .list-item { font-weight: 400; font-size: 50px; line-height: 89px; white-space: nowrap; }
  .list-col.types .list-item { padding-left: 10px; }
  .list-item .cont { padding-left: 9px; }

  .promise {
    position: absolute; left: 168px; top: 914px; width: 863px; height: 174px;
    background: var(--white); border-radius: 62px;
    padding: 30px 0 0 61px;
    font-weight: 800; font-size: 47px; line-height: 54px; letter-spacing: -0.8px; color: var(--teal);
  }
  .website {
    position: absolute; left: 0; width: 1200px; top: 1192px;
    text-align: center; font-weight: 800; font-size: 50px; line-height: 60px; letter-spacing: 0.5px;
  }
</style>
</head>
<body>
<main class="banner">
  <header class="brand">
    <span class="brand-mark"></span>
    <span class="brand-name">COVE POINT ROOFING</span>
  </header>

  <h1 class="headline">Roofing Makes<br>Perfect Sense.</h1>
  <p class="tagline">Get your roof done right now!</p>

  <div class="hero-photo" role="img" aria-label="Photo of a two-storey suburban house with a dark shingle roof and lit windows at dusk under a purple sky"></div>

  <section class="info-panel">
    <h2 class="audience">Serving Property Managers &amp;<br>Realtors Across the Bay Area</h2>

    <ul class="list-col types">
      <li class="list-title">Roof Types:</li>
      <li class="list-item">o Flat Roofs</li>
      <li class="list-item">o Low-Slope</li>
      <li class="list-item">o TPO</li>
      <li class="list-item">o PVC</li>
      <li class="list-item">o Built-Up</li>
      <li class="list-item">o Coatings</li>
    </ul>

    <ul class="list-col services">
      <li class="list-title">Services:</li>
      <li class="list-item">o Inspections</li>
      <li class="list-item">o Leak Repair</li>
      <li class="list-item">o Re-Roofing</li>
      <li class="list-item">o Maintenance</li>
      <li class="list-item"><span class="cont">Plans</span></li>
    </ul>

    <p class="promise">Commercial Roofing That<br>Protects Your Investment</p>

    <p class="website">www.covepointroofing.com</p>
  </section>
</main>
</body>
</html>
```